Responsive web design for leading product search engine

Trovanix is the leading product search engine in Australia and is soon to expand into Asia. We need a lightweight responsive homepage designed for our 3 regional domains. Our domains are Trovanix.com, Trovanix.com.au and Trovanix.asia. We need 3 versions of the same page to appeal to each region. The page and images used need to use a responsive html 5 based web page. The images used in the design need to be responsive and include CSS3 style elements.

For inspiration I would divert you to www.bramvelt.com and www.pinhardo.com.au and I have attached a mockup of what I think it could look like.
Updates

Target Market(s)

Target market is female shoppers 16-40 years old

Industry/Entity Type

Retail

Coding

Coded - Design and coding required

Number of Pages Required

3 page

Colors
33b8a4

Requirements
Must have
• Different image for each of the 3 duplicate pages. 1 for each region Australia (.com.au) Asia (.asia) US (.com). These images must be licensed for public use.

```html
<!DOCTYPE html>
<html lang="en">
<head>
<meta charset="utf-8">
<title>Trovanix – Search millions of products on sale at nearby stores</title>
<link rel="stylesheet" href="https://fonts.googleapis.com/css2?family=Open+Sans:wght@300;400;600;700&display=swap">
<style>
  :root {
    --teal: #33b8a4;
    --teal-dark: #2aa592;
    --teal-footer: #2fb39f;
    --ink: #3a3a3a;
    --muted: #8a8a8a;
    --line: #e4e4e4;
    --band: #f2f2f2;
    --white: #ffffff;
  }
  * { box-sizing: border-box; margin: 0; padding: 0; }
  html, body { width: 695px; height: 1200px; overflow: hidden; }
  body { font-family: "Open Sans", Arial, sans-serif; color: var(--ink); background: var(--white); position: relative; }

  /* Header */
  .site-header { height: 46px; display: flex; align-items: center; justify-content: space-between; padding: 0 58px 0 94px; border-top: 3px solid var(--teal); }
  .brand { display: flex; align-items: center; gap: 6px; font-size: 20px; font-weight: 600; color: var(--teal); }
  .brand-mark { width: 16px; height: 16px; border-radius: 50%; background: var(--teal); }
  .main-nav { display: flex; align-items: center; gap: 22px; font-size: 9px; color: var(--ink); }
  .main-nav .active { color: var(--teal); border-bottom: 2px solid var(--teal); padding-bottom: 3px; }
  .login-btn { border: 1px solid var(--teal); color: var(--teal); border-radius: 12px; padding: 3px 14px; font-size: 8px; }

  /* Hero */
  .hero { position: relative; height: 324px; overflow: hidden; }
  .hero-photo { position: absolute; inset: 0; background: linear-gradient(100deg, #d6a9b9 0%, #c57d98 35%, #b9a4b0 60%, #8fa9a4 100%); }
  .hero-overlay { position: absolute; inset: 0; background: rgba(150, 90, 120, 0.25); }
  .hero-content { position: relative; text-align: center; padding-top: 92px; color: var(--white); }
  .hero-title { font-weight: 300; font-size: 25px; line-height: 1.2; }
  .hero-title strong { display: block; font-weight: 400; font-size: 33px; }
  .search-bar { margin: 18px auto 0; width: 372px; height: 30px; display: flex; background: var(--white); border-radius: 3px; overflow: hidden; }
  .search-field { flex: 1; display: flex; align-items: center; gap: 6px; padding: 0 10px; font-size: 8px; color: var(--muted); border-right: 1px solid var(--line); text-align: left; }
  .search-field:last-of-type { border-right: 0; }
  .search-btn { width: 60px; background: var(--teal); color: var(--white); font-size: 8px; font-weight: 600; display: flex; align-items: center; justify-content: center; letter-spacing: .5px; }
  .slider-arrow { position: absolute; top: 196px; width: 26px; height: 26px; border-radius: 50%; background: rgba(255,255,255,0.3); display: flex; align-items: center; justify-content: center; }
  .slider-arrow.prev { left: 14px; }
  .slider-arrow.next { right: 14px; }

  /* Feature rows */
  .feature { position: absolute; left: 0; width: 695px; }
  .feature-title { font-size: 13px; font-weight: 600; color: var(--ink); margin-bottom: 6px; }
  .feature-lead { font-size: 8px; color: var(--teal); line-height: 1.5; margin-bottom: 8px; }
  .feature-text { font-size: 7px; color: var(--muted); line-height: 1.6; margin-bottom: 14px; }
  .read-more { display: inline-block; border: 1px solid var(--teal); color: var(--teal); border-radius: 12px; padding: 4px 12px; font-size: 7px; font-weight: 600; letter-spacing: .4px; }

  .feature-discover { top: 370px; height: 198px; }
  .feature-discover .feature-copy { position: absolute; left: 94px; top: 48px; width: 230px; }
  .feature-discover .feature-media { position: absolute; left: 410px; top: 36px; width: 150px; height: 96px; border-radius: 10px; background: linear-gradient(135deg, #e9e9e9, #bfb3a4 60%, #8d7c6a); }

  .feature-favourites { top: 568px; height: 197px; background: var(--band); }
  .feature-favourites .feature-media { position: absolute; left: 94px; top: 38px; width: 150px; height: 112px; border-radius: 4px; background: linear-gradient(135deg, #3b3b3b, #8a7f78 45%, #cfc7bf); }
  .feature-favourites .feature-copy { position: absolute; left: 345px; top: 52px; width: 250px; }

  .feature-gallery { top: 765px; height: 290px; text-align: center; }
  .feature-gallery .gallery { margin: 36px auto 0; width: 464px; height: 122px; border-radius: 2px; background: linear-gradient(90deg, #c9b8c2, #e2c7a6 25%, #9ab8c9 50%, #d59aa8 75%, #b7c4b0); }
  .feature-gallery .feature-title { margin-top: 20px; }
  .feature-gallery .feature-text { width: 250px; margin: 0 auto 14px; }

  /* Footer */
  .site-footer { position: absolute; top: 1055px; left: 0; width: 695px; height: 145px; background: var(--teal-footer); color: var(--white); text-align: center; padding-top: 24px; }
  .store-badges { display: flex; justify-content: center; gap: 12px; }
  .store-badge { width: 74px; height: 22px; border-radius: 4px; background: #1d1d1d; }
  .footer-links { display: flex; justify-content: center; gap: 28px; font-size: 7px; margin-top: 12px; }
  .copyright { font-size: 6px; margin-top: 8px; opacity: .85; }
  .social { display: flex; justify-content: center; gap: 8px; margin-top: 12px; }
  .social span { width: 17px; height: 17px; border-radius: 50%; border: 1px solid var(--white); }
</style>
</head>
<body>
  <header class="site-header">
    <div class="brand"><span class="brand-mark"></span>Trovanix</div>
    <nav class="main-nav">
      <span class="active">Home</span><span>About Us</span><span>Services</span><span>App</span><span>News</span><span>Contact</span>
      <span class="login-btn">Login</span>
    </nav>
  </header>

  <section class="hero">
    <div class="hero-photo" role="img" aria-label="Smiling young woman shopping, holding a smartphone and shopping bags"></div>
    <div class="hero-overlay"></div>
    <div class="hero-content">
      <h1 class="hero-title">Search millions of products<strong>on sale at nearby stores</strong></h1>
      <form class="search-bar">
        <div class="search-field">
          <svg width="8" height="8" viewBox="0 0 10 10"><circle cx="4" cy="4" r="3" fill="none" stroke="#999" stroke-width="1.3"/><line x1="6.3" y1="6.3" x2="9" y2="9" stroke="#999" stroke-width="1.3"/></svg>
          What are you looking for?
        </div>
        <div class="search-field">
          <svg width="7" height="9" viewBox="0 0 8 10"><path d="M4 0a3.5 3.5 0 0 0-3.5 3.5C.5 6 4 10 4 10s3.5-4 3.5-6.5A3.5 3.5 0 0 0 4 0z" fill="#999"/><circle cx="4" cy="3.5" r="1.2" fill="#fff"/></svg>
          Your location, City or Code
        </div>
        <div class="search-btn">SEARCH</div>
      </form>
    </div>
    <div class="slider-arrow prev"><svg width="8" height="10" viewBox="0 0 8 10"><path d="M6 1 2 5l4 4" fill="none" stroke="#fff" stroke-width="1.5"/></svg></div>
    <div class="slider-arrow next"><svg width="8" height="10" viewBox="0 0 8 10"><path d="M2 1l4 4-4 4" fill="none" stroke="#fff" stroke-width="1.5"/></svg></div>
  </section>

  <section class="feature feature-discover">
    <div class="feature-copy">
      <h2 class="feature-title">Discover the best products while you shop</h2>
      <p class="feature-lead">Search every local store from one place and see what's in stock near you today.</p>
      <p class="feature-text">Compare prices, check opening hours and find deals from shops in your own neighbourhood before you leave home.</p>
      <a class="read-more">READ MORE</a>
    </div>
    <div class="feature-media" role="img" aria-label="Smartphone showing a shopping mall interior"></div>
  </section>

  <section class="feature feature-favourites">
    <div class="feature-media" role="img" aria-label="Tablet and phone displaying a fashion store"></div>
    <div class="feature-copy">
      <h2 class="feature-title">Find your favourite products on Trovanix</h2>
      <p class="feature-text">Save the brands you love and get alerts when they go on sale at stores close to you, all from one simple app.</p>
      <a class="read-more">READ MORE</a>
    </div>
  </section>

  <section class="feature feature-gallery">
    <div class="gallery" role="img" aria-label="Grid of shopping photos: shoppers with bags, store fronts and clothing racks"></div>
    <h2 class="feature-title">Sed ut perspiciatis unde omnis iste natuam</h2>
    <p class="feature-text">Browse fashion, beauty and home products from thousands of retailers and find the best price in your area.</p>
    <a class="read-more">READ MORE</a>
  </section>

  <footer class="site-footer">
    <div class="store-badges"><span class="store-badge"></span><span class="store-badge"></span></div>
    <nav class="footer-links"><span>Trovanix for Retailers</span><span>About Trovanix</span><span>Blog</span><span>Contact Us</span><span>Help</span></nav>
    <p class="copyright">© Trovanix.com 2024. All rights reserved. Terms and Privacy.</p>
    <div class="social"><span></span><span></span><span></span><span></span></div>
  </footer>
</body>
</html>
```